Simple AD for Digital Publication

Total Size 5" x 5", may include boarder or not
Image Provided; crop or use as background
Incorporate Logo and text as provided

Target Market(s)

Sound Contractors / Integrators

Industry/Entity Type

Audio Video Lighting

Requirements
Must have
• Bold Look that reflects our brand. see website: merrowfenlight.com - cohesive text and style

```html
<!DOCTYPE html>
<html lang="en">
<head>
<meta charset="utf-8">
<title>Merrow Fenlight Co – Dealer Ad</title>
<link rel="stylesheet" href="https://fonts.googleapis.com/css2?family=Montserrat:wght@400;600;800;900&display=swap">
<style>
  :root {
    --page-bg: #9a9aa3;
    --ad-white: #ffffff;
    --brand-red: #b01c24;
    --brand-red-bright: #d9252c;
    --ink-black: #000000;
    --ink-dark: #333333;
    --voltage-yellow: #ffd400;
    --voltage-yellow-light: #fff06a;
    --frame-silver: #d6d6d6;
  }
  html, body {
    margin: 0;
    padding: 0;
    width: 1200px;
    height: 1117px;
    overflow: hidden;
    background: var(--page-bg);
  }
  .ad {
    position: absolute;
    left: 80px;
    top: 39px;
    width: 1040px;
    height: 1039px;
    display: block;
    font-family: "Montserrat", sans-serif;
  }
  .brand-name { font-weight: 800; fill: var(--ink-dark); }
  .brand-tagline { font-weight: 600; fill: var(--ink-dark); }
  .headline-white { font-weight: 800; fill: var(--ad-white); }
  .headline-voltage { font-weight: 900; }
  .dealer-light { font-weight: 400; fill: var(--ad-white); }
  .dealer-bold { font-weight: 800; fill: var(--ad-white); }
  .cta-label { font-weight: 800; fill: var(--ad-white); }
</style>
</head>
<body>
<svg class="ad" viewBox="0 0 963 962" xmlns="http://www.w3.org/2000/svg">
  <defs>
    <linearGradient id="voltageFill" x1="0" y1="0" x2="0" y2="1">
      <stop offset="0" stop-color="var(--voltage-yellow-light)"/>
      <stop offset="0.5" stop-color="var(--voltage-yellow)"/>
      <stop offset="1" stop-color="#f2b800"/>
    </linearGradient>
    <linearGradient id="photoTones" x1="0" y1="0" x2="0" y2="1">
      <stop offset="0" stop-color="#2f4a2a"/>
      <stop offset="0.4" stop-color="#4f6a3a"/>
      <stop offset="0.6" stop-color="#8a7a70"/>
      <stop offset="1" stop-color="#b9a9a6"/>
    </linearGradient>
    <linearGradient id="ctaFill" x1="0" y1="0" x2="0" y2="1">
      <stop offset="0" stop-color="var(--brand-red-bright)"/>
      <stop offset="1" stop-color="var(--brand-red)"/>
    </linearGradient>
  </defs>

  <!-- background and bands -->
  <rect class="ad-base" width="963" height="962" fill="var(--ad-white)"/>
  <polygon class="band-top" points="0,0 245,0 0,53" fill="var(--brand-red)"/>
  <polygon class="band-red" points="0,485 963,283 963,565 0,770" fill="var(--brand-red)"/>
  <polygon class="band-black" points="0,770 963,565 963,893 642,962 0,962" fill="var(--ink-black)"/>

  <!-- brand lockup -->
  <rect class="brand-mark" x="160" y="58" width="62" height="62" fill="var(--brand-red)"/>
  <text class="brand-name" x="240" y="106" font-size="52" textLength="580" lengthAdjust="spacingAndGlyphs">MERROW FENLIGHT CO</text>
  <text class="brand-tagline" x="284" y="134" font-size="25" textLength="530" lengthAdjust="spacingAndGlyphs">Stage Pocket Systems Connectivity</text>

  <!-- product photo area -->
  <rect class="photo-frame" x="59" y="152" width="846" height="396" rx="46" fill="var(--ad-white)"/>
  <rect class="photo" x="67" y="160" width="830" height="380" rx="40" fill="url(#photoTones)"
        role="img" aria-label="Photo of a stage floor pocket with cables, garland and warm string lights"/>

  <!-- headline panel -->
  <path class="panel-frame" d="M282,849 H177 A40,40 0 0 1 137,809 V494 A40,40 0 0 1 177,454 H787 A40,40 0 0 1 827,494 V809 A40,40 0 0 1 787,849 H682"
        fill="none" stroke="var(--frame-silver)" stroke-width="10"/>
  <rect class="panel" x="148" y="465" width="668" height="373" rx="32" fill="var(--ink-black)"/>

  <text class="headline-white" x="481" y="540" font-size="42" text-anchor="middle" textLength="570" lengthAdjust="spacingAndGlyphs">PROTECT AND CONCEAL</text>
  <rect class="highlight-box" x="277" y="561" width="410" height="58" rx="4" fill="var(--brand-red)"/>
  <text class="headline-white" x="482" y="607" font-size="44" text-anchor="middle" textLength="352" lengthAdjust="spacingAndGlyphs">HIGH AND LOW</text>
  <text class="headline-voltage" x="481" y="730" font-size="124" text-anchor="middle" fill="url(#voltageFill)" textLength="583" lengthAdjust="spacingAndGlyphs">VOLTAGE</text>
  <text class="headline-white" x="481" y="787" font-size="62" text-anchor="middle" textLength="468" lengthAdjust="spacingAndGlyphs">CONNECTIVITY</text>
  <rect class="divider" x="432" y="807" width="100" height="3" fill="var(--ad-white)"/>

  <!-- call to action -->
  <text x="481" y="850" font-size="28" text-anchor="middle"><tspan class="dealer-light">Become a </tspan><tspan class="dealer-bold">Dealer</tspan></text>
  <rect class="cta-button" x="319" y="864" width="326" height="63" rx="31.5" fill="url(#ctaFill)" stroke="var(--ad-white)" stroke-width="3"/>
  <text class="cta-label" x="482" y="911" font-size="44" text-anchor="middle" textLength="276" lengthAdjust="spacingAndGlyphs">CLICK HERE</text>
</svg>
</body>
</html>
```